Rollway Supply and Aged Care products

a catalogue that can be printed and uploaded in a format to our web site. must be able to insert pages and remove as needed to kee up with our product range.
reference sites are:
www.dawnfieldmobility.com
www.rollwaysupply.com.au

```html
<!DOCTYPE html>
<html lang="en">
<head>
<meta charset="utf-8">
<title>Rollway Supply Catalogue Covers</title>
<link href="https://fonts.googleapis.com/css2?family=Philosopher:wght@400;700&display=swap" rel="stylesheet">
<style>
  :root {
    --canvas: #ffffff;
    --page: #eeeeee;
    --navy: #2a3768;
    --teal: #0a7db6;
    --sky: #1a9fe2;
    --ink: #2a3560;
    --brand: #8c5b92;
    --tagline: #2f7fc4;
    --white: #ffffff;
  }
  html, body {
    margin: 0;
    padding: 0;
    width: 1200px;
    height: 777px;
    overflow: hidden;
    background: var(--canvas);
    font-family: "Philosopher", sans-serif;
  }
  .spread {
    position: relative;
    width: 1200px;
    height: 777px;
  }
  .page {
    position: absolute;
    top: 17px;
    width: 574px;
    height: 743px;
    background: var(--page);
    overflow: hidden;
  }
  .page--back { left: 17px; }
  .page--front { left: 608px; }
  .page__art {
    position: absolute;
    inset: 0;
    width: 574px;
    height: 743px;
  }
  .contact {
    position: absolute;
    left: 45px;
    top: 519px;
    color: var(--ink);
    font-size: 11px;
    line-height: 12.4px;
  }
  .contact p { margin: 0; }
  .contact__name { font-weight: 700; }
  .contact__email { margin-top: 12px !important; }
  .contact__numbers {
    margin-top: 12px;
    display: grid;
    grid-template-columns: 57px auto;
  }
  .site-url {
    position: absolute;
    right: 44px;
    top: 704px;
    margin: 0;
    color: var(--white);
    font-size: 12px;
    line-height: 14px;
    letter-spacing: 0.2px;
  }
  .masthead__name {
    position: absolute;
    left: 189px;
    top: 52px;
    margin: 0;
    color: var(--brand);
    font-size: 44px;
    font-weight: 700;
    line-height: 1;
  }
  .masthead__tagline {
    position: absolute;
    left: 200px;
    top: 94px;
    margin: 0;
    color: var(--tagline);
    font-size: 11px;
    line-height: 13px;
  }
</style>
</head>
<body>
<div class="spread">

  <section class="page page--back" aria-label="Back cover">
    <svg class="page__art" viewBox="0 0 510 660" preserveAspectRatio="none" aria-hidden="true">
      <defs>
        <linearGradient id="waveFillBack" x1="0" y1="0" x2="0" y2="1">
          <stop offset="0" stop-color="#2a3768"/>
          <stop offset="0.55" stop-color="#1d5a92"/>
          <stop offset="1" stop-color="#0a7db6"/>
        </linearGradient>
      </defs>
      <path d="M0 617 C70 600 120 560 200 566 C280 572 330 600 385 598 C430 596 450 520 470 495 C480 483 495 478 510 478 L510 660 L0 660 Z" fill="var(--sky)"/>
      <path d="M0 624 C70 607 120 568 200 574 C280 580 330 608 385 606 C432 604 452 530 472 504 C482 492 496 486 510 486 L510 660 L0 660 Z" fill="url(#waveFillBack)"/>
    </svg>

    <div class="contact">
      <p class="contact__name">Rollway Supply</p>
      <p>Unit 7 14 Elm Street, GLENWOOD</p>
      <p class="contact__email">info@rollwaysupply.com.au</p>
      <div class="contact__numbers">
        <span>Telephone</span><span>: +61 2 9000 1482</span>
        <span>Mobile</span><span>: +61 400 555 218</span>
        <span>Fax</span><span>: +61 2 9000 1483</span>
      </div>
    </div>

    <p class="site-url">www.rollwaysupply.com.au</p>
  </section>

  <section class="page page--front" aria-label="Front cover">
    <svg class="page__art" viewBox="0 0 510 660" preserveAspectRatio="none">
      <defs>
        <linearGradient id="headerFade" x1="0" y1="0" x2="0" y2="1">
          <stop offset="0" stop-color="#eeeeee"/>
          <stop offset="0.6" stop-color="#fafafa"/>
          <stop offset="1" stop-color="#ffffff"/>
        </linearGradient>
        <radialGradient id="photoTones" cx="0.6" cy="0.55" r="0.75">
          <stop offset="0" stop-color="#e6d3c3"/>
          <stop offset="0.35" stop-color="#ece6df"/>
          <stop offset="0.7" stop-color="#eef0ef"/>
          <stop offset="1" stop-color="#d9dfdc"/>
        </radialGradient>
        <linearGradient id="waveFillFront" x1="0" y1="0" x2="0" y2="1">
          <stop offset="0" stop-color="#2a3768"/>
          <stop offset="0.55" stop-color="#1d5a92"/>
          <stop offset="1" stop-color="#0a7db6"/>
        </linearGradient>
      </defs>
      <rect class="masthead__band" x="0" y="0" width="510" height="140" fill="url(#headerFade)" aria-hidden="true"/>
      <circle class="masthead__mark" cx="82" cy="70" r="30" fill="#5aa9dc" aria-hidden="true"/>
      <rect class="cover__rule" x="0" y="140" width="510" height="14" fill="var(--navy)" aria-hidden="true"/>
      <rect class="cover__photo" x="0" y="154" width="510" height="506" fill="url(#photoTones)" role="img" aria-label="Photo: a woman in a wheelchair working on a laptop in a bright office while a colleague points at the screen"/>
      <g aria-hidden="true">
        <path d="M0 480 C25 474 45 486 70 530 C95 575 120 588 170 588 C260 588 340 560 400 590 C440 610 470 622 510 624 L510 660 L0 660 Z" fill="var(--sky)"/>
        <path d="M0 488 C24 482 42 494 66 538 C92 584 120 597 170 597 C260 597 340 569 400 599 C440 619 470 631 510 633 L510 660 L0 660 Z" fill="url(#waveFillFront)"/>
      </g>
    </svg>

    <h1 class="masthead__name">Rollway Supply</h1>
    <p class="masthead__tagline">Sales, Service and Repairs</p>
  </section>

</div>
</body>
</html>
```